Etiquette pour pots de Miel de Kolvera
Besoins
Nous souhaitons créer une étiquette pour notre Miel de Kolvera, produit et commercialisé en République Démocratique du Congo.
Ce miel s’apparente à une qualité bio car les ruches se trouvent en pleine nature, loin des villes et de la pollution.
Les caractéristiques du flacon sont les suivantes (photo ci-joint) :
Hauteur : 12 cm
Circonférence (mi-hauteur) : 34 cm
Diamètre (ouverture supérieure) : 8 cm
Contenance : 660 ml.
La taille de l’étiquette est laissée à la libre appréciation du graphiste.
L’étiquette doit évoquer le côté sain/circuit court/bio et la qualité.
Les éléments suivants doivent être présents sur l’étiquette :
1. Nom du produit :
MIEL DE KOLVERA
ASALI YA KOLVERA (traduction en swahili)
2. Eléments : abeille stylisée, fleurs
3. Logo Tumsoa (ci-joint)
4. Producteur : Ranch de Kolvera
5. Miel Bio des plateaux de Kolvera
6. 660 ml

```html
<!DOCTYPE html>
<html lang="fr">
<head>
<meta charset="utf-8">
<title>Miel de Kolvera – étiquette</title>
<link rel="stylesheet" href="https://fonts.googleapis.com/css2?family=Rubik+Dirt&family=Montserrat:wght@500;600;700&display=swap">
<style>
  :root {
    --bg: #f3efe6;
    --label-white: #ffffff;
    --label-green: #8cc63f;
    --ink: #111111;
    --honey-red: #e0252b;
    --brand-green: #6fae3a;
    --bee-yellow: #f2e23a;
  }
  * { margin: 0; padding: 0; box-sizing: border-box; }
  html, body { width: 899px; height: 1200px; overflow: hidden; background: var(--bg); }
  .canvas { position: relative; width: 899px; height: 1200px; }
  .label-shape { position: absolute; inset: 0; }
  .label-text { position: absolute; inset: 0; font-family: "Montserrat", Arial, sans-serif; color: var(--ink); }
  .product-name {
    position: absolute;
    font-family: "Rubik Dirt", "Impact", sans-serif;
    line-height: 1;
    color: var(--ink);
  }
  .product-name--main { left: 150px; top: 455px; font-size: 190px; letter-spacing: 4px; }
  .product-name--link { left: 520px; top: 650px; font-family: "Montserrat", Arial, sans-serif; font-weight: 700; font-size: 26px; }
  .product-name--place { left: 190px; top: 680px; font-size: 92px; letter-spacing: 2px; }
  .swahili-name {
    position: absolute; right: 190px; top: 782px;
    font-weight: 600; font-size: 22px; color: var(--honey-red); letter-spacing: 0.5px;
  }
  .producer-info {
    position: absolute; left: 270px; top: 850px;
    font-weight: 600; font-size: 21px; line-height: 1.2; text-align: center;
  }
  .volume { position: absolute; left: 640px; top: 878px; font-weight: 600; font-size: 20px; }
  .brand {
    position: absolute; left: 0; right: 0; top: 935px;
    display: flex; justify-content: center; align-items: center; gap: 8px;
  }
  .brand-dot { width: 12px; height: 12px; border-radius: 50%; background: var(--brand-green); }
  .brand-name { font-weight: 700; font-size: 20px; letter-spacing: 3px; color: var(--brand-green); }
</style>
</head>
<body>
<main class="canvas">
  <svg class="label-shape" width="899" height="1200" viewBox="0 0 899 1200" aria-hidden="false">
    <defs>
      <radialGradient id="illustration-tone" cx="50%" cy="50%" r="60%">
        <stop offset="0%" stop-color="#f2e23a"/>
        <stop offset="55%" stop-color="#ef6a3a"/>
        <stop offset="100%" stop-color="#e0252b"/>
      </radialGradient>
    </defs>
    <g class="label-border" fill="var(--label-green)">
      <circle cx="450" cy="600" r="322"/>
      <circle cx="250" cy="420" r="192"/>
      <circle cx="480" cy="360" r="212"/>
      <circle cx="690" cy="480" r="192"/>
      <circle cx="700" cy="740" r="192"/>
      <circle cx="450" cy="820" r="202"/>
      <circle cx="220" cy="720" r="192"/>
    </g>
    <g class="label-face" fill="var(--label-white)">
      <circle cx="450" cy="600" r="300"/>
      <circle cx="250" cy="420" r="170"/>
      <circle cx="480" cy="360" r="190"/>
      <circle cx="690" cy="480" r="170"/>
      <circle cx="700" cy="740" r="170"/>
      <circle cx="450" cy="820" r="180"/>
      <circle cx="220" cy="720" r="170"/>
    </g>
    <ellipse class="bee-flower-illustration" cx="640" cy="405" rx="110" ry="62"
      fill="url(#illustration-tone)" opacity="0.85"
      role="img" aria-label="Abeille stylisée et fleur rouge au cœur jaune"/>
  </svg>

  <div class="label-text">
    <h1 class="product-name product-name--main">MIEL</h1>
    <span class="product-name product-name--link">de</span>
    <span class="product-name product-name--place">KOLVERA</span>
    <p class="swahili-name">ASALI YA KOLVERA</p>
    <p class="producer-info">Producteur : Ranch de Kolvera<br>Miel Bio des plateaux de Kolvera</p>
    <p class="volume">660 ml</p>
    <div class="brand">
      <span class="brand-dot"></span>
      <span class="brand-name">TUMSOA</span>
    </div>
  </div>
</main>
</body>
</html>
```